Brindle Offers is an online marketing platform.

A daily deals site for consumers a way to bring in new clients for clients and this is who the business cards are for. Industries - Food and Drink, Things To Do, Beauty and Spas, Staycations and Services.
Logo on one side.
Name - Owen Radley
Job Title - Sales Director
Phone Number - 07912358046
Email - owen@brindleoffers.co.uk
need same for second person
Name - Fiona Bracken
Job Title - Operations Director
Phone Number - 01632840275
Email - fiona@brindleoffers.co.uk
Bottom Right - Chatterbook Icon, Snapa Icon, Pipline Icon
Target Market(s)
Business owners of the above industries
Contact Information for Business Card
Name - Owen Radley
Name - Fiona Bracken
Look and feel

```html
<!DOCTYPE html>
<html lang="en">
<head>
<meta charset="utf-8">
<title>Brindle Offers – Business Cards</title>
<link href="https://fonts.googleapis.com/css2?family=Open+Sans:wght@400;600;700;800&display=swap" rel="stylesheet">
<style>
  :root {
    --stage: #242424;
    --card: #ffffff;
    --brand-blue: #0b56a6;
    --ink-grey: #4a4a4a;
    --soft-grey: #6b6b6b;
    --rule-grey: #8a8a8a;
    --band-grey: #4d4d4d;
  }
  * { margin: 0; padding: 0; box-sizing: border-box; }
  html, body { width: 1200px; height: 895px; overflow: hidden; background: var(--stage); }
  body { position: relative; font-family: "Open Sans", Arial, sans-serif; }

  .card {
    position: absolute;
    width: 560px;
    height: 320px;
    background: var(--card);
    border-radius: 22px;
    overflow: hidden;
    box-shadow: 0 14px 30px rgba(0,0,0,0.45);
  }
  .card--front { left: 90px; top: 100px; }
  .card--back { left: 550px; top: 470px; }

  /* Front */
  .front-web {
    position: absolute; left: 0; right: 0; top: 70px; text-align: center;
    font-weight: 600; font-size: 13px; color: var(--ink-grey); letter-spacing: 1px;
  }
  .front-logo {
    position: absolute; left: 0; right: 0; top: 105px;
    display: flex; align-items: center; justify-content: center; gap: 12px;
  }
  .logo-dot { width: 26px; height: 26px; border-radius: 50%; background: var(--brand-blue); flex: none; }
  .logo-name { font-weight: 800; font-size: 34px; color: var(--brand-blue); letter-spacing: 0.5px; white-space: nowrap; }
  .social-row {
    position: absolute; left: 0; right: 0; top: 215px;
    display: flex; justify-content: center; gap: 22px; list-style: none;
  }
  .social-row li { display: flex; align-items: center; gap: 6px; font-size: 11px; font-weight: 600; color: var(--ink-grey); }
  .social-dot { width: 14px; height: 14px; border-radius: 50%; }
  .social-dot--chatterbook { background: #2f4e8f; }
  .social-dot--pipline { background: #4aa3df; }
  .social-dot--snapa { background: #5a3a30; }

  /* Back */
  .back-logo { position: absolute; left: 34px; top: 122px; display: flex; align-items: center; gap: 8px; }
  .back-logo .logo-dot { width: 20px; height: 20px; }
  .back-logo .logo-name { font-size: 27px; }

  .divider { position: absolute; left: 282px; top: 70px; width: 1px; height: 140px; background: var(--rule-grey); }

  .contact { position: absolute; left: 302px; top: 66px; }
  .person-name { font-weight: 800; font-size: 22px; color: var(--brand-blue); letter-spacing: -0.3px; }
  .person-title { font-size: 13px; color: var(--soft-grey); margin-top: -2px; }
  .contact-list { list-style: none; margin-top: 14px; }
  .contact-list li { display: flex; align-items: center; gap: 9px; font-size: 13px; color: var(--ink-grey); line-height: 24px; white-space: nowrap; }
  .contact-list svg { width: 11px; height: 11px; fill: var(--brand-blue); flex: none; }

  .base-band { position: absolute; left: 0; right: 0; bottom: 0; height: 12px; display: flex; }
  .base-band .band-blue { width: 73%; background: var(--brand-blue); }
  .base-band .band-gap { width: 1.5%; background: var(--card); }
  .base-band .band-grey { flex: 1; background: var(--band-grey); }
</style>
</head>
<body>

<section class="card card--front" aria-label="Business card front">
  <p class="front-web">www.brindleoffers.co.uk</p>
  <div class="front-logo">
    <span class="logo-dot"></span>
    <span class="logo-name">Brindle Offers</span>
  </div>
  <ul class="social-row">
    <li><span class="social-dot social-dot--chatterbook"></span>Chatterbook</li>
    <li><span class="social-dot social-dot--pipline"></span>Pipline</li>
    <li><span class="social-dot social-dot--snapa"></span>Snapa</li>
  </ul>
</section>

<section class="card card--back" aria-label="Business card back">
  <div class="back-logo">
    <span class="logo-dot"></span>
    <span class="logo-name">Brindle Offers</span>
  </div>

  <div class="divider"></div>

  <div class="contact">
    <h1 class="person-name">OWEN RADLEY</h1>
    <p class="person-title">Sales Director</p>
    <ul class="contact-list">
      <li>
        <svg viewBox="0 0 24 24" aria-hidden="true"><path d="M6.6 10.8a15.1 15.1 0 0 0 6.6 6.6l2.2-2.2a1 1 0 0 1 1-.25 11.4 11.4 0 0 0 3.6.57 1 1 0 0 1 1 1V20a1 1 0 0 1-1 1A17 17 0 0 1 3 4a1 1 0 0 1 1-1h3.5a1 1 0 0 1 1 1c0 1.25.2 2.45.57 3.6a1 1 0 0 1-.25 1z"/></svg>
        07912358046
      </li>
      <li>
        <svg viewBox="0 0 24 24" aria-hidden="true"><path d="M2 5h20v14H2z M2 5l10 8 10-8"/></svg>
        owen@brindleoffers.co.uk
      </li>
      <li>
        <svg viewBox="0 0 24 24" aria-hidden="true"><circle cx="12" cy="12" r="10"/></svg>
        www.brindleoffers.co.uk
      </li>
    </ul>
  </div>

  <div class="base-band">
    <span class="band-blue"></span><span class="band-gap"></span><span class="band-grey"></span>
  </div>
</section>

</body>
</html>
```